Design a single page Shopify store web page

We are looking to have a page designed for a single page Shopify store with 2 products. We already have a basic structure that we like, though we are open to suggestions. We are looking for somebody to provide a design/color scheme that we can then implement using Shopify's templating system. We can handle the implementation(HTML / CSS / jS) as we already have 2 web developers on the team, but have not been able to find a design we liked.

The job would consist of providing a mockup (photoshop or otherwise) and any vector graphics you choose to create for the site (we can provide product photos and other images).

You can also look at http://tidewrenco.com.au for some of our design direction we have used so far

Target Market(s)

Young Australian Males (18 - 49)

Industry/Entity Type

Store

Number of Pages Required

1 page

Font styles to use
Serif
Sans Serif

Requirements
Must have
• Single Page Design
• E-commerce Product Purchase
• Manly (whatever interpretation of that you have)

```html
<!DOCTYPE html>
<html lang="en">
<head>
<meta charset="utf-8">
<title>Tidewren Co — Underwear and Socks Delivered</title>
<link href="https://fonts.googleapis.com/css2?family=Arimo:wght@400&display=swap" rel="stylesheet">
<style>
  :root {
    --bg-dark: #2f2f2f;
    --bg-mid: #3d3d3d;
    --ink-white: #ffffff;
    --ink-grey: #8c8c8c;
    --bubble: #141414;
    --band: rgba(20, 20, 20, 0.85);
    --teal: #27a7bd;
    --rule: #1f1f1f;
  }
  * { margin: 0; padding: 0; box-sizing: border-box; }
  html, body { width: 1200px; height: 912px; overflow: hidden; }
  body {
    position: relative;
    font-family: "Arimo", Arial, sans-serif;
    background: var(--bg-dark);
    color: var(--ink-white);
  }
  .hero-photo {
    position: absolute; inset: 0;
    background:
      radial-gradient(ellipse 420px 260px at 640px 520px, #242424 0%, rgba(36,36,36,0) 100%),
      radial-gradient(ellipse 260px 180px at 700px 860px, #4a3a30 0%, rgba(74,58,48,0) 100%),
      linear-gradient(180deg, var(--bg-dark) 0%, var(--bg-mid) 60%, #353535 100%);
  }
  .menu {
    position: absolute; left: 37px; top: 40px; width: 44px;
    text-align: center; font-size: 13px; letter-spacing: 0.3px;
  }
  .menu-icon { display: block; margin: 0 auto 9px; }
  .brand {
    position: absolute; left: 0; right: 0; top: 92px;
    text-align: center; font-size: 92px; line-height: 1; letter-spacing: 2px;
  }
  .headline {
    position: absolute; left: 0; right: 0; top: 392px;
    text-align: center; color: var(--ink-grey);
    font-size: 66px; line-height: 77px;
  }
  .bubble {
    position: absolute; top: 590px;
  }
  .bubble-text {
    position: absolute; width: 170px; text-align: center;
    font-size: 22px; line-height: 26px;
  }
  .signup-band {
    position: absolute; left: 180px; top: 705px; width: 854px; height: 99px;
    background: var(--band); border-radius: 6px;
  }
  .email-field {
    position: absolute; left: 211px; top: 731px; width: 458px; height: 50px;
    background: var(--ink-white); border-radius: 6px;
    color: #111; font-size: 17px; line-height: 50px; padding-left: 18px;
  }
  .subscribe-button {
    position: absolute; left: 696px; top: 731px; width: 323px; height: 50px;
    background: var(--teal); border-radius: 6px;
    font-size: 21px; line-height: 50px; text-align: center;
  }
  .scroll-cue {
    position: absolute; left: 0; right: 0; top: 831px;
    text-align: center; font-size: 16px; letter-spacing: 0.3px;
  }
  .scroll-cue svg { display: block; margin: 10px auto 0; }
  .page-rule {
    position: absolute; left: 0; right: 0; top: 907px; height: 5px;
    background: var(--rule); border-top: 1px solid #555;
  }
</style>
</head>
<body>
  <div class="hero-photo" role="img" aria-label="Dimmed photo of a hand holding a pair of black socks"></div>

  <div class="menu">
    <svg class="menu-icon" width="33" height="21" viewBox="0 0 33 21">
      <g stroke="#fff" stroke-width="1.5">
        <line x1="0" y1="1" x2="33" y2="1"/>
        <line x1="0" y1="10.5" x2="33" y2="10.5"/>
        <line x1="0" y1="20" x2="33" y2="20"/>
      </g>
    </svg>
    MENU
  </div>

  <div class="brand">TIDEWREN CO</div>

  <h1 class="headline" style="font-weight:400">
    New Underwear and Socks<br>
    Delivered to your door<br>
    Every 3 or 6 Months
  </h1>

  <div class="signup-band"></div>

  <svg class="bubble" style="left:45px" width="232" height="170" viewBox="0 0 232 170">
    <path d="M113 4 C175 4 225 34 225 69 C225 104 180 130 130 132 L160 165 C130 150 110 135 100 132 C48 126 2 100 2 69 C2 34 52 4 113 4 Z" fill="var(--bubble)"/>
  </svg>
  <div class="bubble-text" style="left:74px; top:620px">Let me know when you launch</div>

  <svg class="bubble" style="left:930px" width="232" height="170" viewBox="0 0 232 170">
    <defs>
      <linearGradient id="tealGlow" x1="0" y1="0" x2="0" y2="1">
        <stop offset="0.55" stop-color="#141414"/>
        <stop offset="1" stop-color="#27a7bd"/>
      </linearGradient>
    </defs>
    <path d="M114 4 C176 4 226 34 226 69 C226 100 192 124 148 131 C135 140 125 150 112 162 C118 150 122 140 120 133 C60 130 6 104 6 69 C6 34 54 4 114 4 Z" fill="url(#tealGlow)"/>
  </svg>
  <div class="bubble-text" style="left:960px; top:620px">get a free gift with your first pack</div>

  <div class="email-field">E-MAIL:</div>
  <div class="subscribe-button">You have been subscribed</div>

  <div class="scroll-cue">
    SCROLL DOWN
    <svg width="42" height="24" viewBox="0 0 42 24">
      <g fill="none" stroke="#fff" stroke-width="1.5">
        <polyline points="1,1 21,13 41,1"/>
        <polyline points="1,10 21,22 41,10"/>
      </g>
    </svg>
  </div>

  <div class="page-rule"></div>
</body>
</html>
```